Diesel injection diagnostics and repairs

I am after a business card design for my business.
The business; repairs diesel fuel systems on 4wds, trucks, earthmoving equipment,can do mobile repairs and diagnostics
The business design can basic but effective, I guess some colours such as green and black or even blue......
The end result should reflect the business name and logo and what the business can do

Industry/Entity Type

Business

Contact Information for Business Card

TB Diesel Injection PTY LTD
tb_diesel@mailbox-example.net
Nathan Bowers
0491570156

```html
<!DOCTYPE html>
<html lang="en">
<head>
<meta charset="utf-8">
<title>TB Diesel Injection – Business Card Concepts</title>
<link rel="stylesheet" href="https://fonts.googleapis.com/css2?family=Anton&family=Questrial&display=swap">
<style>
  :root {
    --canvas: #f1f1f2;
    --card: #ffffff;
    --card-edge: #9a9a9a;
    --ink: #000000;
    --paper-text: #ffffff;
    --accent-yellow: #f5e51b;
    --accent-blue: #27a8e0;
    --accent-green: #3bb54a;
    --display: "Anton", "Arial Narrow", sans-serif;
    --body: "Questrial", "Century Gothic", sans-serif;
  }
  * { margin: 0; padding: 0; box-sizing: border-box; }
  html, body { width: 982px; height: 1200px; overflow: hidden; background: var(--canvas); }
  .sheet { position: relative; width: 982px; height: 1200px; }

  .card { position: absolute; background: var(--card); border: 1px solid var(--card-edge); overflow: hidden; }
  .card--portrait { width: 403px; height: 660px; top: 49px; }
  .card--yellow { left: 66px; }
  .card--blue { left: 530px; }
  .card--landscape { left: 66px; top: 753px; width: 662px; height: 400px; }

  .card__panel { position: absolute; left: 0; top: 0; width: 100%; height: 100%; }

  .brand-mark {
    position: absolute; font-family: var(--display); line-height: 1;
    letter-spacing: 16px; white-space: nowrap; transform-origin: left top;
  }
  .brand-line {
    position: absolute; font-family: var(--display); line-height: 1;
    color: var(--paper-text); white-space: nowrap; transform-origin: left top;
  }
  .service { position: absolute; font-family: var(--body); color: var(--ink); white-space: nowrap; line-height: 1; }

  .illustration { position: absolute; border-radius: 10px; }

  /* Yellow portrait */
  .card--yellow .brand-mark { left: 116px; top: 83px; font-size: 153px; color: var(--accent-yellow); transform: scaleX(1.45); }
  .card--yellow .brand-line { left: 123px; top: 233px; font-size: 24px; transform: scaleX(1.4); }
  .card--yellow .illustration {
    left: 159px; top: 282px; width: 68px; height: 380px; transform: rotate(-20deg);
    background: linear-gradient(180deg, rgba(245,229,27,.55), rgba(245,229,27,.25));
  }
  .card--yellow .service { left: 4px; top: 517px; font-size: 25px; transform: rotate(67deg); }

  /* Blue portrait */
  .card--blue .brand-mark { left: 84px; top: 76px; font-size: 153px; color: var(--accent-blue); transform: scaleX(1.45); }
  .card--blue .brand-line { left: 190px; color: var(--accent-blue); }
  .card--blue .brand-line--first { top: 229px; font-size: 34px; transform: scaleX(1.35); }
  .card--blue .brand-line--second { top: 266px; font-size: 24px; transform: scaleX(1.33); }
  .card--blue .illustration {
    left: 136px; top: 252px; width: 68px; height: 394px; transform: rotate(-20deg);
    background: linear-gradient(180deg, rgba(39,168,224,.55), rgba(39,168,224,.25));
  }
  .card--blue .service { left: 200px; top: 431px; font-size: 28px; transform: rotate(90deg); }

  /* Green landscape */
  .card--landscape .brand-mark { left: 84px; top: 95px; font-size: 144px; color: var(--accent-green); transform: scaleX(1.5); }
  .card--landscape .illustration {
    left: 296px; top: 180px; width: 366px; height: 54px; border-radius: 0;
    background: linear-gradient(90deg, rgba(59,181,74,.35), rgba(59,181,74,.1));
  }
  .card--landscape .brand-line { left: 84px; top: 240px; font-size: 29px; color: var(--ink); transform: scaleX(1.4); }
  .card--landscape .service { left: 341px; top: 246px; font-size: 25px; font-style: italic; }
</style>
</head>
<body>
<main class="sheet">

  <section class="card card--portrait card--yellow" aria-label="Portrait card, yellow">
    <svg class="card__panel" viewBox="0 0 403 660" aria-hidden="true">
      <polygon points="111,80 342,80 342,660 205,660 111,372" fill="var(--ink)"/>
    </svg>
    <div class="illustration" role="img" aria-label="Cutaway drawing of a diesel fuel injector in yellow line work"></div>
    <div class="brand-mark">TB</div>
    <div class="brand-line">Diesel Injection</div>
    <div class="service">Diagnostics &amp; Repairs</div>
  </section>

  <section class="card card--portrait card--blue" aria-label="Portrait card, blue">
    <svg class="card__panel" viewBox="0 0 403 660" aria-hidden="true">
      <polygon points="77,80 309,80 309,660 185,660 77,393" fill="var(--ink)"/>
    </svg>
    <div class="illustration" role="img" aria-label="Cutaway drawing of a diesel fuel injector in blue line work"></div>
    <div class="brand-mark">TB</div>
    <div class="brand-line brand-line--first">Diesel</div>
    <div class="brand-line brand-line--second">Injection</div>
    <div class="service">Diagnostics &amp; Repairs</div>
  </section>

  <section class="card card--landscape" aria-label="Landscape card, green">
    <svg class="card__panel" viewBox="0 0 662 400" aria-hidden="true">
      <rect x="81" y="94" width="581" height="141" fill="var(--ink)"/>
    </svg>
    <div class="illustration" role="img" aria-label="Green hand-drawn scribble line trailing from the name"></div>
    <div class="brand-mark">TB</div>
    <div class="brand-line">Diesel Injection</div>
    <div class="service">Diagnostics &amp; Repairs</div>
  </section>

</main>
</body>
</html>
```